Business Card for Technology Startup

Design a 2-sided business card using the logo provided. We are a digital healthcare platform that provides a mobile app and web UI that helps caregivers, families, and doctors share information and provide better patient outcomes. We use AI and machine learning to help guide patients through their day-to-day life. The final design should communicate stability, peace, comfort, but also align with the image of an AI-driven technology startup.

I'd like the deliverable to by a Photoshop PSD file (with layers) that I can work with in pixlr.com. Should contain the following editable layers:
Name (ex. John Doe)
Title (ex. Founder / CEO)
Email (ex. info@brenvaxa.ai)
Phone (ex. (999) 333-5555)
Website (ex. https://brenvaxa.ai)

```html
<!DOCTYPE html>
<html lang="en">
<head>
<meta charset="utf-8">
<title>Brenvaxa Business Card</title>
<link rel="stylesheet" href="https://fonts.googleapis.com/css2?family=Nunito:wght@400;600;700&display=swap">
<style>
  :root {
    --backdrop: #8b4a2c;
    --card-white: #ffffff;
    --cyan-deep: #06b9e6;
    --cyan-bright: #00f6ff;
    --corner-grey: #6a6a6a;
    --ink: #111111;
    --icon-grey: #6f6f6f;
    --shadow: rgba(0, 0, 0, 0.28);
  }
  * { box-sizing: border-box; margin: 0; padding: 0; }
  html, body {
    width: 1200px;
    height: 1051px;
    overflow: hidden;
  }
  body {
    position: relative;
    background: var(--backdrop);
    font-family: "Nunito", sans-serif;
    color: var(--ink);
  }
  .brand-wordmark {
    position: absolute;
    left: 776px;
    top: 72px;
    font-weight: 700;
    font-size: 70px;
    letter-spacing: 1px;
    color: var(--card-white);
    line-height: 1;
  }
  .card {
    position: absolute;
    width: 467px;
    height: 302px;
    border-radius: 10px;
    overflow: hidden;
    box-shadow: 0 4px 14px var(--shadow);
  }
  .card-back {
    left: 218px;
    top: 268px;
    background: linear-gradient(90deg, var(--cyan-deep), var(--cyan-bright));
    display: flex;
    align-items: center;
    justify-content: center;
  }
  .card-back .back-name {
    font-weight: 700;
    font-size: 44px;
    color: var(--card-white);
    letter-spacing: 1px;
  }
  .card-front {
    left: 526px;
    top: 540px;
    background: var(--card-white);
  }
  .card-front .shapes {
    position: absolute;
    inset: 0;
  }
  .front-logo {
    position: absolute;
    left: 52px;
    top: 137px;
    font-weight: 700;
    font-size: 27px;
    color: var(--ink);
    line-height: 1;
  }
  .divider {
    position: absolute;
    left: 233px;
    top: 49px;
    width: 1.5px;
    height: 205px;
    background: var(--ink);
  }
  .person {
    position: absolute;
    left: 260px;
    top: 94px;
  }
  .person-name {
    font-weight: 600;
    font-size: 24px;
    line-height: 1;
  }
  .person-title {
    font-size: 11.5px;
    margin-top: 3px;
    margin-left: 1px;
  }
  .contacts {
    position: absolute;
    left: 261px;
    top: 180px;
    list-style: none;
  }
  .contacts li {
    display: flex;
    align-items: center;
    height: 21.3px;
    font-size: 11px;
    letter-spacing: 0.3px;
  }
  .contacts svg {
    width: 15px;
    height: 15px;
    margin-right: 9px;
    flex: none;
  }
</style>
</head>
<body>
  <div class="brand-wordmark">brenvaxa</div>

  <section class="card card-back" aria-label="Card back">
    <span class="back-name">brenvaxa</span>
  </section>

  <section class="card card-front" aria-label="Card front">
    <svg class="shapes" viewBox="0 0 467 302" aria-hidden="true">
      <defs>
        <linearGradient id="cyanCorner" x1="0" y1="0" x2="1" y2="0">
          <stop offset="0" stop-color="#06b9e6"/>
          <stop offset="1" stop-color="#00f6ff"/>
        </linearGradient>
      </defs>
      <path d="M407 0 A60 60 0 0 0 467 60 L467 0 Z" fill="#6a6a6a"/>
      <path d="M0 202 A100 100 0 0 1 100 302 L0 302 Z" fill="url(#cyanCorner)"/>
    </svg>

    <div class="front-logo">brenvaxa</div>
    <div class="divider"></div>

    <div class="person">
      <div class="person-name">John Doe</div>
      <div class="person-title">Founder/CEO</div>
    </div>

    <ul class="contacts">
      <li>
        <svg viewBox="0 0 16 16" aria-hidden="true"><circle cx="8" cy="8" r="8" fill="#6f6f6f"/><path d="M5.2 4.2l1.4 1.6-.7 1a5 5 0 0 0 2.4 2.4l1-.7 1.6 1.4-.8 1.2C7.4 11 5 8.6 4 5z" fill="#fff"/></svg>
        555 210-4477
      </li>
      <li>
        <svg viewBox="0 0 16 16" aria-hidden="true"><circle cx="8" cy="8" r="8" fill="#6f6f6f"/><path d="M8 3.5a3 3 0 0 1 3 3c0 2.2-3 5.8-3 5.8S5 8.7 5 6.5a3 3 0 0 1 3-3z" fill="#fff"/><circle cx="8" cy="6.5" r="1.1" fill="#6f6f6f"/></svg>
        Lakeview, United States
      </li>
      <li>
        <svg viewBox="0 0 16 16" aria-hidden="true"><circle cx="8" cy="8" r="8" fill="#6f6f6f"/><rect x="3.8" y="5" width="8.4" height="6" fill="none" stroke="#fff" stroke-width="0.9"/><path d="M3.8 5l4.2 3.4L12.2 5M3.8 11l3-2.8M12.2 11l-3-2.8" fill="none" stroke="#fff" stroke-width="0.9"/></svg>
        info@brenvaxa.ai
      </li>
      <li>
        <svg viewBox="0 0 16 16" aria-hidden="true"><circle cx="8" cy="8" r="8" fill="#6f6f6f"/><g fill="none" stroke="#fff" stroke-width="0.8"><circle cx="8" cy="8" r="4.5"/><ellipse cx="8" cy="8" rx="2" ry="4.5"/><path d="M3.5 8h9M4.2 5.6h7.6M4.2 10.4h7.6"/></g></svg>
        https://brenvaxa.ai
      </li>
    </ul>
  </section>
</body>
</html>
```